Letter Head Design

I need a letter head design based on my company logo that I attached.
Include phone number: (403)582-4316
Address: 347 14th Avenue NE, Calgary, Alberta, Canada, T3K 4R8

Industry/Entity Type

It Company

```html
<!DOCTYPE html>
<html lang="en">
<head>
<meta charset="utf-8">
<title>Brightfold Interiors Corp. – Letterhead</title>
<link href="https://fonts.googleapis.com/css2?family=Open+Sans:wght@400;600;700&family=Questrial&display=swap" rel="stylesheet">
<style>
  :root {
    --paper: #ffffff;
    --ink: #4a4a4a;
    --ink-dark: #333333;
    --brand-blue: #2f6db5;
    --brand-green: #6cb52f;
    --signature-tone: #ececec;
  }
  * { margin: 0; padding: 0; box-sizing: border-box; }
  html, body { width: 942px; height: 1200px; overflow: hidden; background: var(--paper); }
  .letterhead {
    position: relative;
    width: 942px;
    height: 1200px;
    background: var(--paper);
    font-family: "Open Sans", Arial, sans-serif;
    color: var(--ink);
  }
  .brand {
    position: absolute;
    top: 120px;
    left: 0;
    width: 100%;
    display: flex;
    justify-content: center;
    align-items: center;
    gap: 14px;
  }
  .brand-square { width: 30px; height: 30px; background: var(--brand-green); }
  .brand-name {
    font-family: "Open Sans", Arial, sans-serif;
    font-weight: 600;
    font-size: 32px;
    color: var(--brand-blue);
    letter-spacing: -0.5px;
  }
  .meta {
    position: absolute;
    top: 258px;
    left: 125px;
    font-family: "Questrial", Arial, sans-serif;
    font-size: 11px;
    line-height: 14px;
    color: var(--ink-dark);
  }
  .meta strong { font-weight: 700; font-family: "Open Sans", Arial, sans-serif; }
  .body-copy {
    position: absolute;
    top: 306px;
    left: 125px;
    width: 735px;
    font-size: 12.2px;
    line-height: 25px;
  }
  .salutation { margin-bottom: 0; }
  .body-copy p.paragraph { text-align: justify; margin-bottom: 24px; }
  .signatory {
    position: absolute;
    top: 727px;
    left: 125px;
    font-family: "Questrial", Arial, sans-serif;
  }
  .signatory-name { font-size: 23px; color: var(--ink-dark); letter-spacing: 0.5px; line-height: 26px; }
  .signatory-name strong { font-family: "Open Sans", Arial, sans-serif; font-weight: 700; }
  .signatory-role { font-size: 12px; color: #666; line-height: 14px; }
  .signature {
    position: absolute;
    top: 798px;
    left: 125px;
    width: 253px;
    height: 115px;
    background: var(--signature-tone);
  }
  .footer {
    position: absolute;
    top: 1125px;
    left: 74px;
    display: flex;
    align-items: center;
    height: 56px;
  }
  .footer-square { width: 56px; height: 56px; background: var(--brand-green); }
  .footer-divider { width: 1px; height: 56px; background: var(--brand-blue); margin: 0 14px 0 16px; }
  .contact { font-size: 10px; line-height: 15.5px; color: var(--brand-blue); letter-spacing: 0.3px; }
  .contact-line { display: flex; align-items: center; gap: 8px; }
  .contact-line svg { width: 10px; height: 10px; fill: var(--brand-blue); flex: none; }
  .contact-line.indent { padding-left: 18px; }
</style>
</head>
<body>
<main class="letterhead">
  <header class="brand">
    <span class="brand-square"></span>
    <span class="brand-name">Brightfold</span>
  </header>

  <section class="meta">
    <div><strong>Date :</strong> Mon , 25 / 3 / 2013</div>
    <div><strong>Recipient : Mr.Alan Reed Whitmore</strong></div>
  </section>

  <section class="body-copy">
    <p class="salutation">Dear Mr. Alan Reed</p>
    <p class="paragraph">LoTrem ipsum dolor sit amet, consectetur adipiscing elit. Praesent vulputate, neque ac accumsan suscipit, justo turpis volutpat nisl, tempus fermentum eros tortor et elit. Vivamus porttitor faucibus gravida. Quisque pharetra gravida luctus. Donec eget turpis libero. Ut ac dolor urna, quis tempor nunc. Donec vitae mauris purus, euismod eleifend nulla. Lorem ipsum dolor sit amet, consectetur adipiscing elit. Donec ut purus tellus. Aenean quis dignissim lacus. Vestibulum suscipit vehicula cursus. Suspendisse potenti. Ut in sem nisi. Sed et massa leo.</p>
    <p class="paragraph">Fusce varius libero vel risus condimentum suscipit. Nullam tristique ultrices massa a volutpat. Donec sed dictum metus. Curabitur fringilla nibh eu ligula pharetra a interdum quam aliquam. Maecenas aliquam elit eu orci rutrum molestie. Proin nisl justo, varius a volutpat nec, ultricies sed sem. Nam sit amet imperdiet sem. Phasellus vitae mauris odio. Etiam in purus dui. Etiam ultricies, ante vel iaculis sodales, arcu leo adipiscing leo, sit amet mollis dui nisi non quam.</p>
    <p class="paragraph">Suspendisse sagittis laoreet dolor, vitae rhoncus arcu volutpat quis. Vestibulum at placerat dolor. Vivamus eu lacus ut enim molestie consectetur. Quisque ac lorem vel orci sagittis sollicitudin. Nunc ut quam sem, quis volutpat libero. Cum sociis natoque penatibus et magnis dis parturient montes, nascetur ridiculus mus. Vestibulum ante ipsum primis in faucibus orci luctus et ultrices posuere cubilia Curae; Donec tempor velit in velit feugiat sit amet vulputate nisl posuere..</p>
  </section>

  <section class="signatory">
    <div class="signatory-name"><strong>ALAN</strong> REED</div>
    <div class="signatory-role">General director</div>
  </section>
  <div class="signature" role="img" aria-label="Handwritten signature of the general director"></div>

  <footer class="footer">
    <span class="footer-square"></span>
    <span class="footer-divider"></span>
    <address class="contact" style="font-style: normal;">
      <div class="contact-line">
        <svg viewBox="0 0 10 10" aria-hidden="true"><path d="M5 0a3.6 3.6 0 0 0-3.6 3.6C1.4 6.3 5 10 5 10s3.6-3.7 3.6-6.4A3.6 3.6 0 0 0 5 0zm0 5a1.4 1.4 0 1 1 0-2.8A1.4 1.4 0 0 1 5 5z"/></svg>
        <span>347 14TH AVENUE NE, CALGARY</span>
      </div>
      <div class="contact-line indent"><span>ALBERTA, CANADA, T3K 4R8</span></div>
      <div class="contact-line">
        <svg viewBox="0 0 10 10" aria-hidden="true"><path d="M0 3.2C0 1.6 2 .8 5 .8s5 .8 5 2.4v.8H7.4V3c-.7-.3-1.5-.4-2.4-.4S3.3 2.7 2.6 3v1H0zM2.6 4.6h4.8L9 9.2H1z"/></svg>
        <span>(403) 582 4316</span>
      </div>
    </address>
  </footer>
</main>
</body>
</html>
```